Brindle Logistics Business Card Design

We are a trucking and warehousing company. We run freight in the US manly from the Pacific NW to TX and back up the the PNW. We also do warehousing where we store, move, and distribute freight. Looking for a clean and modern design of business card. We would like to look rich and elegant. Attached is our logo.

Industry/Entity Type

Trucking Company

Contact Information for Business Card

Looking for a clean and modern design of business card. We would like to look rich and elegant.

Font styles to use
Sans Serif

Colors

Designer to choose colors to be used in the design.

Requirements
Must have
• logo but it should not dominate the card
Should not have
• logo should not dominate the card

```html
<!DOCTYPE html>
<html lang="en">
<head>
<meta charset="utf-8">
<title>Brindle Logistics Business Card</title>
<link href="https://fonts.googleapis.com/css2?family=Open+Sans:wght@400;600&family=PT+Serif:wght@700&display=swap" rel="stylesheet">
<style>
  :root {
    --page-bg: #e6e8eb;
    --card-white: #ffffff;
    --brand-blue: #1a6fc0;
    --brand-blue-light: #4fa3e0;
    --brand-blue-deep: #1568b3;
    --charcoal: #2f3033;
    --ink: #1d1d1f;
    --ink-soft: #3a3a3c;
  }
  * { box-sizing: border-box; margin: 0; padding: 0; }
  html, body { width: 1200px; height: 873px; overflow: hidden; }
  body {
    background: var(--page-bg);
    font-family: "Open Sans", Arial, sans-serif;
    display: flex;
    align-items: center;
    justify-content: center;
    gap: 40px;
  }
  .card {
    position: relative;
    width: 520px;
    height: 300px;
    overflow: hidden;
    box-shadow: 0 6px 18px rgba(0,0,0,0.18);
  }
  /* Front */
  .card-front { background: var(--card-white); }
  .front-shapes { position: absolute; inset: 0; }
  .office-address {
    position: absolute;
    left: 96px; top: 226px;
    color: #fff;
    font-size: 13px;
    letter-spacing: 0.3px;
  }
  .front-wordmark {
    position: absolute;
    left: 128px; top: 172px;
    display: flex; align-items: center; gap: 7px;
    color: var(--brand-blue);
    font-weight: 600;
    font-size: 15px;
    letter-spacing: 1px;
    text-transform: uppercase;
  }
  .wordmark-dot {
    width: 10px; height: 10px; border-radius: 50%;
    background: var(--brand-blue);
  }
  .identity {
    position: absolute;
    right: 60px; top: 24px;
    text-align: left;
  }
  .person-name {
    font-family: "PT Serif", Georgia, serif;
    font-weight: 700;
    font-size: 19px;
    color: var(--ink);
  }
  .person-title {
    font-size: 14px;
    color: var(--ink-soft);
    margin-top: 2px;
  }
  .contact-row {
    position: absolute;
    left: 0; right: 0; top: 92px; height: 72px;
    display: flex;
    justify-content: space-around;
    align-items: center;
    padding: 0 20px;
  }
  .contact-item {
    display: flex; flex-direction: column; align-items: center; gap: 6px;
    color: var(--brand-blue);
    font-size: 12px;
  }
  .contact-icon {
    width: 24px; height: 24px; border-radius: 50%;
    background: var(--brand-blue);
    display: flex; align-items: center; justify-content: center;
  }
  /* Back */
  .card-back {
    background: radial-gradient(ellipse at 45% 45%, var(--brand-blue-light) 0%, var(--brand-blue-deep) 60%, #12599c 100%);
    display: flex; align-items: center; justify-content: center;
  }
  .back-wordmark {
    display: flex; align-items: center; gap: 12px;
    color: #fff;
    font-weight: 600;
    font-size: 26px;
    letter-spacing: 2px;
    text-transform: uppercase;
  }
  .back-wordmark .wordmark-dot { width: 16px; height: 16px; background: #fff; }
</style>
</head>
<body>

  <section class="card card-front">
    <svg class="front-shapes" width="520" height="300" viewBox="0 0 520 300">
      <rect x="0" y="262" width="520" height="38" fill="var(--charcoal)"/>
      <path d="M30,262 Q30,206 92,206 L300,206 Q352,206 352,262 Z" fill="#fff"/>
      <path d="M38,262 Q38,212 96,212 L298,212 Q344,212 344,262 Z" fill="var(--brand-blue)"/>
      <line x1="0" y1="86" x2="520" y2="86" stroke="var(--brand-blue)" stroke-width="2"/>
      <line x1="0" y1="168" x2="520" y2="168" stroke="var(--brand-blue)" stroke-width="2"/>
    </svg>

    <div class="identity">
      <div class="person-name">Your Name</div>
      <div class="person-title">General Manager</div>
    </div>

    <div class="contact-row">
      <div class="contact-item">
        <span class="contact-icon">
          <svg width="14" height="14" viewBox="0 0 24 24"><path fill="#fff" d="M6.6 10.8a15.1 15.1 0 0 0 6.6 6.6l2.2-2.2a1 1 0 0 1 1-.25 11.4 11.4 0 0 0 3.6.57 1 1 0 0 1 1 1V20a1 1 0 0 1-1 1A17 17 0 0 1 3 4a1 1 0 0 1 1-1h3.5a1 1 0 0 1 1 1c0 1.25.2 2.45.57 3.6a1 1 0 0 1-.25 1z"/></svg>
        </span>
        <span>(000) 000-0000</span>
      </div>
      <div class="contact-item">
        <span class="contact-icon">
          <svg width="14" height="14" viewBox="0 0 24 24"><rect x="3" y="6" width="18" height="12" fill="none" stroke="#fff" stroke-width="2"/><path d="M3 6l9 7 9-7" fill="none" stroke="#fff" stroke-width="2"/></svg>
        </span>
        <span>abc@brindlelogistics.com</span>
      </div>
      <div class="contact-item">
        <span class="contact-icon">
          <svg width="14" height="14" viewBox="0 0 24 24"><circle cx="12" cy="12" r="9" fill="none" stroke="#fff" stroke-width="1.8"/><ellipse cx="12" cy="12" rx="4" ry="9" fill="none" stroke="#fff" stroke-width="1.5"/><path d="M3 12h18M5 7.5h14M5 16.5h14" stroke="#fff" stroke-width="1.3"/></svg>
        </span>
        <span>www.brindlelogistics.com</span>
      </div>
    </div>

    <div class="front-wordmark"><span class="wordmark-dot"></span>Brindle Logistics</div>
    <div class="office-address">Your Office Address</div>
  </section>

  <section class="card card-back">
    <div class="back-wordmark"><span class="wordmark-dot"></span>Brindle Logistics</div>
  </section>

</body>
</html>
```